Hemp company needs website/online store

We are a startup hemp company and we need an online storefront designed. We are very open do design, but will include our logo to help. We make 100% hemp derived products like edibles, concentrates, vapes and THCA flower. Everything is grown locally, and all products are extracted and made in house.

Requirements
Nice to have
• I would like to highlight that we have Cannabis products that are hemp derived and 100% legal across the US. Also that all cannabis is locally grown and products are extracted and made in house and sent out for third party lab testing.

```html
<!DOCTYPE html>
<html lang="en">
<head>
<meta charset="utf-8">
<title>Meadowleaf Hemp</title>
<link href="https://fonts.googleapis.com/css2?family=Poppins:ital,wght@0,400;0,500;0,600;1,400&display=swap" rel="stylesheet">
<style>
:root{
  --green:#2d7a0c;
  --green-dark:#1e5b06;
  --heading:#1f5a0a;
  --lime:#9cb83a;
  --footer:#3a7d0a;
  --footer-bar:#1f5a05;
  --gray-bg:#f3f3f3;
  --text:#444;
  --muted:#666;
  --gold:#f5b400;
}
*{margin:0;padding:0;box-sizing:border-box}
html,body{width:1200px;height:3998px;overflow:hidden}
body{font-family:'Poppins',sans-serif;color:var(--text);position:relative;background:#fff}
.abs{position:absolute}
.header{left:0;top:0;width:1200px;height:157px;background:#fff}
.brand{left:47px;top:50px;display:flex;align-items:center;gap:12px;font-size:34px;font-weight:600;color:var(--green)}
.brand .mark{width:30px;height:30px;border-radius:50%;background:var(--lime)}
.nav{left:480px;top:62px;display:flex;gap:37px;font-size:15px;color:#333}
.nav .active{color:var(--green);font-weight:600;font-size:17px;margin-top:-2px}
.btn{display:flex;align-items:center;justify-content:center;border-radius:30px;font-weight:500}
.contact-btn{left:1023px;top:57px;width:130px;height:38px;background:var(--green);color:#fff;font-size:15px}
.hero{left:0;top:157px;width:1200px;height:673px;background:radial-gradient(ellipse at 75% 45%,#5d9a2f 0%,#2f6a14 40%,#173f08 75%,#0f2d05 100%)}
.hero h1{left:109px;top:170px;width:560px;font-size:37px;font-weight:400;line-height:1.17;color:#fff}
.hero h1 b{font-weight:600}
.hero p{left:111px;top:327px;width:520px;font-size:15px;line-height:1.5;color:#fff}
.hero .btn{left:112px;top:411px;width:177px;height:48px;background:var(--lime);color:var(--green-dark);font-size:17px}
.intro{left:0;top:830px;width:1200px;height:446px;background:var(--gray-bg)}
.video{left:67px;top:90px;width:416px;height:286px;border-radius:4px;background:radial-gradient(circle at 50% 50%,#d49a2a,#9a5f10 55%,#4a2a05)}
.play{left:174px;top:111px}
.intro h2{left:526px;top:103px;font-size:40px;font-weight:500;color:var(--heading)}
.intro p{left:528px;top:188px;width:570px;font-size:15.5px;line-height:1.45;color:var(--muted)}
.intro .read{left:529px;top:300px;width:177px;height:50px;background:var(--green);color:#fff;font-size:17px}
.intro .ours{left:719px;top:300px;width:178px;height:50px;border:1.5px solid #999;color:var(--green-dark);font-size:17px;background:#fff}
.products{left:0;top:1276px;width:1200px;height:920px;background:#fff}
.sec-title{width:1200px;left:0;text-align:center;font-size:56px;font-weight:500;color:var(--heading)}
.filter{top:201px;height:50px;width:212px;border:2px solid var(--green-dark);color:#333;font-size:18px;background:#fff}
.filter.on{background:var(--green);color:#fff;border-color:var(--green)}
.card{top:299px;width:278px;height:557px;border:1px solid #e3e3e3;background:#fff}
.card .img{left:0;top:0;width:276px;height:351px}
.card .name{left:13px;top:366px;font-size:20px;font-weight:500;color:#333}
.card .stars{left:162px;top:366px;font-size:19px;color:var(--gold);letter-spacing:1px}
.card .desc{left:16px;top:406px;width:200px;font-size:13.5px;line-height:1.45;color:var(--muted)}
.card .price{left:16px;top:454px;font-size:19px;font-weight:600;color:#222}
.card .cart{left:16px;top:490px;width:161px;height:46px;background:var(--green);color:#fff;font-size:15px;border-radius:0;gap:10px}
.diff{left:0;top:2196px;width:1200px;height:714px;background:var(--gray-bg)}
.feat{top:169px;width:325px;height:491px;background:#fff}
.feat h3{left:15px;font-size:19px;font-weight:500;color:var(--green)}
.feat p{left:15px;width:280px;font-size:15px;line-height:1.45;color:#333}
.feat .img{left:15px;width:295px;height:258px;border-radius:8px}
.testi{left:0;top:2910px;width:1200px;height:585px;background:#fff}
.tcard{top:172px;width:500px;height:270px;background:#f7f7f7}
.tcard .stars{left:66px;top:38px;font-size:26px;color:var(--gold);letter-spacing:2px}
.tcard .who{left:66px;top:82px;font-size:21px;color:var(--green)}
.tcard .role{left:66px;top:112px;font-size:18px;font-style:italic;color:#555}
.tcard p{left:66px;top:175px;width:360px;font-size:15px;line-height:1.5;color:#333}
.avatar{top:-12px;width:112px;height:112px;border-radius:50%}
.footer{left:0;top:3495px;width:1200px;height:394px;background:var(--footer);color:#fff}
.footer .fbrand{left:84px;top:170px;font-size:38px;font-weight:600;display:flex;align-items:center;gap:10px}
.footer .fbrand .mark{width:24px;height:24px;border-radius:50%;background:var(--lime)}
.fcol h4{font-size:20px;font-weight:400;white-space:nowrap}
.fcol .rule{width:40px;height:2px;background:#fff;margin:16px 0 22px}
.fcol li{list-style:none;font-size:15px;margin-bottom:13px;white-space:nowrap}
.fcol li::before{content:"›";margin-right:12px;font-size:17px}
.fcol p{font-size:15px;line-height:1.35;width:260px}
.finput{left:852px;top:231px;width:251px;height:38px;background:#fff;border:1px solid #ddd}
.fsub{left:852px;top:281px;width:126px;height:37px;background:var(--footer-bar);font-size:13px;display:flex;align-items:center;justify-content:center}
.bar{left:0;top:3889px;width:1200px;height:109px;background:var(--footer-bar);color:#fff}
.social{top:32px;width:40px;height:40px;border:2px solid #fff;border-radius:50%}
.copy{right:87px;top:42px;font-size:17px;font-weight:500}
</style>
</head>
<body>

<header class="abs header">
  <div class="abs brand"><span class="mark"></span>Meadowleaf Hemp</div>
  <nav class="abs nav">
    <span class="active">Home</span><span>About Us</span><span>Our Products</span><span>blogs</span><span>Testimonials</span>
  </nav>
  <div class="abs btn contact-btn">Contact Us</div>
</header>

<section class="abs hero" role="img" aria-label="Close-up photo of green hemp leaves">
  <h1 class="abs"><b>Cannabis Products</b> that are hemp derived and 100% legal across the US.</h1>
  <p class="abs">All cannabis is locally grown and products are extracted and made in house and sent out for third party lab testing.</p>
  <div class="abs btn">Our Products</div>
</section>

<section class="abs intro">
  <div class="abs video" role="img" aria-label="Video still of a golden hemp flower bud">
    <svg class="abs play" width="68" height="68" viewBox="0 0 68 68"><circle cx="34" cy="34" r="33" fill="#fff"/><path d="M26 20 L50 34 L26 48 Z" fill="#1e5b06"/></svg>
  </div>
  <h2 class="abs">Make you mind &amp; body Better</h2>
  <p class="abs">Lorem ipsum dolor sit amet, consectetur adipiscing elit, sed do eiusmod tempor incididuntcommodo viverra&nbsp; accumsan lacus incididunt commodo viverra&nbsp; accumsan lacus vel facilisis.</p>
  <div class="abs btn read">Read More</div>
  <div class="abs btn ours">Our Products</div>
</section>

<section class="abs products">
  <h2 class="abs sec-title" style="top:95px">All Products</h2>
  <div class="abs btn filter on" style="left:143px">All Products</div>
  <div class="abs btn filter" style="left:374px">Concentrates</div>
  <div class="abs btn filter" style="left:605px">Vapes</div>
  <div class="abs btn filter" style="left:837px">THCA flower.</div>

  <article class="abs card" style="left:37px">
    <div class="abs img" style="background:linear-gradient(160deg,#3a2a18,#1a120a)" role="img" aria-label="Photo of a tincture box and dropper bottle"></div>
    <div class="abs name">VERDA VAPES</div><div class="abs stars">★★★★★</div>
    <div class="abs desc">Welcome to this beautiful 5 in the warm .</div>
    <div class="abs price">$420,00</div>
    <div class="abs btn cart">Add to cart <span>›</span></div>
  </article>
  <article class="abs card" style="left:320px">
    <div class="abs img" style="background:linear-gradient(160deg,#4a4a40,#222418)" role="img" aria-label="Photo of oil jars beside a hemp leaf"></div>
    <div class="abs name">VERDA VAPES</div><div class="abs stars">★★★★★</div>
    <div class="abs desc">Welcome to this beautiful 5 in the warm .</div>
    <div class="abs price">$420,00</div>
    <div class="abs btn cart">Add to cart <span>›</span></div>
  </article>
  <article class="abs card" style="left:602px">
    <div class="abs img" style="background:linear-gradient(160deg,#d8d4c8,#7a6a4a)" role="img" aria-label="Photo of a jar of hemp flower with an hourglass"></div>
    <div class="abs name">VERDA VAPES</div><div class="abs stars">★★★★★</div>
    <div class="abs desc">Welcome to this beautiful 5 in the warm .</div>
    <div class="abs price">$420,00</div>
    <div class="abs btn cart">Add to cart <span>›</span></div>
  </article>
  <article class="abs card" style="left:885px">
    <div class="abs img" style="background:linear-gradient(160deg,#6a7a5a,#3a3a28)" role="img" aria-label="Photo of an oil dropper bottle among succulents"></div>
    <div class="abs name">VERDA VAPES</div><div class="abs stars">★★★★★</div>
    <div class="abs desc">Welcome to this beautiful 5 in the warm .</div>
    <div class="abs price">$420,00</div>
    <div class="abs btn cart">Add to cart <span>›</span></div>
  </article>
</section>

<section class="abs diff">
  <h2 class="abs sec-title" style="top:52px">What Makes Us Different</h2>
  <div class="abs feat" style="left:93px">
    <h3 class="abs" style="top:45px">100 % ORGANIC</h3>
    <p class="abs" style="top:85px">After an arrest, the court will set a on the charges and other than contributing factors .</p>
    <div class="abs img" style="top:199px;background:linear-gradient(160deg,#3a3028,#4a6a5a 60%,#7a4a2a)" role="img" aria-label="Photo of hemp chocolate and nuts on a slate"></div>
  </div>
  <div class="abs feat" style="left:436px">
    <div class="abs img" style="top:15px;background:radial-gradient(circle at 50% 50%,#6a8a4a,#c9a89a 45%,#2a2222 80%)" role="img" aria-label="Photo of cupped hands holding hemp flower"></div>
    <h3 class="abs" style="top:320px">LAB TESTED</h3>
    <p class="abs" style="top:360px">After the bail amount is set, the Bail Bonds Lone Star for free initial bail information.</p>
  </div>
  <div class="abs feat" style="left:778px">
    <h3 class="abs" style="top:45px">BEST QUALITY</h3>
    <p class="abs" style="top:85px">We then work with you or your loved one and the jail full amount of the bail set by the court.</p>
    <div class="abs img" style="top:199px;background:radial-gradient(circle at 55% 50%,#5a8a4a,#2a4a2a 70%)" role="img" aria-label="Photo of a hemp leaf held in a gloved hand"></div>
  </div>
</section>

<section class="abs testi">
  <h2 class="abs sec-title" style="top:42px">Client’s Testimonials</h2>
  <div class="abs tcard" style="left:96px">
    <div class="abs avatar" style="left:340px;background:#f0b030" role="img" aria-label="Portrait of the client"></div>
    <div class="abs stars">★★★★★</div>
    <div class="abs who">Nolan Reyes</div>
    <div class="abs role">Organiser</div>
    <p class="abs">Lorem ipsum dolor sit amet, conse tetur adipiscing elit, sed do eiusmod tempor vel facilisis.</p>
  </div>
  <div class="abs tcard" style="left:611px">
    <div class="abs avatar" style="left:342px;background:#8aa8b0" role="img" aria-label="Portrait of the client"></div>
    <div class="abs stars">★★★★★</div>
    <div class="abs who">Marcus Hale</div>
    <div class="abs role">Organiser</div>
    <p class="abs">Lorem ipsum dolor sit amet, conse tetur adipiscing elit, sed do eiusmod tempor maecenas vel facilisis.</p>
  </div>
  <svg class="abs" style="left:545px;top:464px" width="106" height="46" viewBox="0 0 106 46">
    <circle cx="22" cy="23" r="22" fill="#2d7a0c"/><path d="M25 15 L17 23 L25 31" stroke="#fff" stroke-width="3" fill="none"/>
    <circle cx="84" cy="23" r="22" fill="#2d7a0c"/><path d="M81 15 L89 23 L81 31" stroke="#fff" stroke-width="3" fill="none"/>
  </svg>
</section>

<footer class="abs footer">
  <div class="abs fbrand"><span class="mark"></span>Meadowleaf</div>
  <div class="abs fcol" style="left:354px;top:87px">
    <h4>Quick Links</h4><div class="rule"></div>
    <ul><li>Home</li><li>About Us</li><li>Our Services</li><li>Our Blogs</li><li>Testimonials</li></ul>
  </div>
  <div class="abs fcol" style="left:585px;top:87px">
    <h4>Customer Services</h4><div class="rule"></div>
    <ul><li>Contact us</li><li>Site Map</li><li>Terms and Use</li><li>My Account</li></ul>
  </div>
  <div class="abs fcol" style="left:852px;top:85px">
    <h4>Our Newsletter</h4><div class="rule"></div>
    <p>Subscribe our newsletter to get the latest news.</p>
  </div>
  <div class="abs finput"></div>
  <div class="abs fsub">SUBSCRIBE</div>
</footer>

<div class="abs bar">
  <div class="abs social" style="left:89px"></div>
  <div class="abs social" style="left:141px"></div>
  <div class="abs social" style="left:193px"></div>
  <div class="abs social" style="left:244px"></div>
  <div class="abs copy">All Rights Reserved @ Copyrights 2023</div>
</div>

</body>
</html>
```